British Columbia Day banner showcasing 20% off site

Banner graphic promoting our BC Day sale
Size: 1800 x 1000
- flag has been uploaded for inspiration
- examples from other companies and their sale banners have been uploaded for inspiration.
- product images can be found at www.kelvoraleaf.com, please use a variety of different products in this banner

Target Market(s)

19+

Industry/Entity Type

Cannabis

Requirements
Must have
• Phrases:
- “Celebrate BC Day with BC bud and companies”
- “20% off site wide sale*"
- Underneath phrase the date of sale “July 30th - August 3rd”
- In tiny print “*excludes all sale and bundled items”
- MUST BE 1800 X1000
Nice to have
• - images of the products or bud we carry which can be found at www.kelvoraleaf.com
- bold
Should not have
• - company logo

```html
<!DOCTYPE html>
<html lang="en">
<head>
<meta charset="utf-8">
<title>BC Day Site Wide Sale Banner</title>
<link href="https://fonts.googleapis.com/css2?family=Archivo+Black&family=Inter:wght@400;500;600;800&display=swap" rel="stylesheet">
<style>
  :root {
    --page-bg: #abc4fc;
    --banner-bg: #ffffff;
    --ink: #000000;
    --bc-blue: #1a6fb8;
    --navy: #272e75;
    --red: #e5101a;
    --yellow: #f8c300;
    --peach-tint: #fbe3d8;
    --lavender-tint: #e6e8f8;
    --bud-light: #8a8f55;
    --bud-dark: #4e4a36;
  }
  html, body {
    margin: 0;
    padding: 0;
    width: 1200px;
    height: 1200px;
    overflow: hidden;
    background: var(--page-bg);
  }
  .banner {
    position: absolute;
    left: 0;
    top: 266px;
    width: 1200px;
    height: 667px;
    background: var(--banner-bg);
    overflow: hidden;
    font-family: "Inter", Arial, sans-serif;
  }
  .accent-circle {
    position: absolute;
    border-radius: 50%;
  }
  .accent-circle.peach { background: var(--peach-tint); opacity: .55; }
  .accent-circle.lavender { background: var(--lavender-tint); opacity: .7; }
  .bud {
    position: absolute;
    border-radius: 48% 52% 45% 55% / 55% 45% 55% 45%;
    background: radial-gradient(ellipse at 40% 40%, var(--bud-light), var(--bud-dark));
  }
  .headline {
    position: absolute;
    left: 0;
    width: 1200px;
    text-align: center;
    margin: 0;
    font-weight: 500;
    font-size: 58px;
    line-height: 1;
    color: var(--ink);
    letter-spacing: -0.5px;
  }
  .headline .line-one { position: absolute; left: 0; right: 0; top: 85px; }
  .headline .line-two { position: absolute; left: 0; right: 0; top: 146px; }
  .headline .highlight { color: var(--bc-blue); font-weight: 600; }
  .discount {
    position: absolute;
    left: 300px;
    top: 240px;
    width: 600px;
    height: 135px;
  }
  .sale-label {
    position: absolute;
    left: 0;
    width: 1200px;
    top: 400px;
    text-align: center;
    margin: 0;
    font-weight: 500;
    font-size: 72px;
    line-height: 1;
    color: var(--ink);
    letter-spacing: -0.5px;
  }
  .sale-dates {
    position: absolute;
    left: 371px;
    top: 492px;
    width: 459px;
    height: 71px;
    background: var(--navy);
    color: #fff;
    font-weight: 800;
    font-size: 33px;
    display: flex;
    align-items: center;
    justify-content: center;
    letter-spacing: 0.2px;
  }
  .sale-dates sup { font-size: 19px; vertical-align: 12px; margin-left: 1px; }
  .fine-print {
    position: absolute;
    left: 0;
    width: 1200px;
    top: 574px;
    text-align: center;
    font-size: 19px;
    font-weight: 400;
    color: var(--ink);
    margin: 0;
  }
</style>
</head>
<body>
  <section class="banner" aria-label="BC Day site wide sale">
    <div class="accent-circle peach" style="left:668px;top:-33px;width:236px;height:236px"></div>
    <div class="accent-circle peach" style="left:-71px;top:310px;width:124px;height:124px"></div>
    <div class="accent-circle lavender" style="left:285px;top:305px;width:236px;height:236px"></div>
    <div class="accent-circle lavender" style="left:1138px;top:260px;width:120px;height:120px"></div>
    <div class="accent-circle lavender" style="left:728px;top:563px;width:220px;height:220px"></div>

    <div class="bud" role="img" aria-label="Cannabis bud product photo" style="left:0;top:0;width:127px;height:48px"></div>
    <div class="bud" role="img" aria-label="Cannabis bud product photo" style="left:78px;top:258px;width:143px;height:99px"></div>
    <div class="bud" role="img" aria-label="Cannabis bud product photo" style="left:0;top:563px;width:137px;height:104px"></div>
    <div class="bud" role="img" aria-label="Cannabis bud product photo" style="left:470px;top:629px;width:84px;height:50px"></div>
    <div class="bud" role="img" aria-label="Cannabis bud product photo" style="left:1035px;top:0;width:165px;height:118px"></div>
    <div class="bud" role="img" aria-label="Cannabis bud product photo" style="left:1027px;top:245px;width:98px;height:88px"></div>
    <div class="bud" role="img" aria-label="Cannabis bud product photo" style="left:894px;top:499px;width:91px;height:80px"></div>
    <div class="bud" role="img" aria-label="Cannabis bud product photo" style="left:1064px;top:523px;width:136px;height:144px"></div>

    <h1 class="headline">
      <span class="line-one">Celebrate <span class="highlight">BC DAY</span></span>
      <span class="line-two">with BC bud and companies</span>
    </h1>

    <svg class="discount" viewBox="0 0 600 135" aria-label="20% OFF">
      <defs>
        <linearGradient id="fill-twenty" gradientUnits="userSpaceOnUse" x1="60" y1="20" x2="240" y2="150">
          <stop offset="0" stop-color="var(--red)"/>
          <stop offset=".42" stop-color="var(--red)"/>
          <stop offset=".42" stop-color="var(--yellow)"/>
          <stop offset=".78" stop-color="var(--yellow)"/>
          <stop offset=".78" stop-color="var(--navy)"/>
          <stop offset="1" stop-color="var(--navy)"/>
        </linearGradient>
        <linearGradient id="fill-off" gradientUnits="userSpaceOnUse" x1="340" y1="0" x2="440" y2="90">
          <stop offset="0" stop-color="var(--yellow)"/>
          <stop offset=".15" stop-color="var(--yellow)"/>
          <stop offset=".15" stop-color="var(--navy)"/>
          <stop offset=".5" stop-color="var(--navy)"/>
          <stop offset=".5" stop-color="var(--red)"/>
          <stop offset="1" stop-color="var(--red)"/>
        </linearGradient>
      </defs>
      <text x="304" y="127" text-anchor="middle" font-family="'Archivo Black', Arial, sans-serif" font-size="164" textLength="585" lengthAdjust="spacingAndGlyphs" fill="#000" stroke="#000" stroke-width="4">20% OFF</text>
      <text x="300" y="124" text-anchor="middle" font-family="'Archivo Black', Arial, sans-serif" font-size="164" textLength="585" lengthAdjust="spacingAndGlyphs" fill="#fff" stroke="#fff" stroke-width="4">20% OFF</text>
      <text x="300" y="124" text-anchor="middle" font-family="'Archivo Black', Arial, sans-serif" font-size="164" textLength="585" lengthAdjust="spacingAndGlyphs"><tspan fill="url(#fill-twenty)">20%</tspan> <tspan fill="url(#fill-off)">OFF</tspan></text>
    </svg>

    <p class="sale-label">Site Wide Sale</p>

    <div class="sale-dates">JULY 30<sup>TH</sup>&nbsp;-&nbsp;AUGUST 3<sup>RD</sup></div>

    <p class="fine-print">*excludes all sale and bundled items</p>
  </section>
</body>
</html>
```